Coralbend Pastoral Traders Business Cards

We require business cards revamped with our logo. A few details we would like to use.

1. Round Edges
2. Our logo over the top of a wagyu cattle background photo on one side of the card

Other side of the card has the below details.

1. Person Name (First & Last)
2. Job Position
3. Mobile Number
4. Email Address
5. Website Address

Simple & Neat.

Target Market(s)

Sales

Industry/Entity Type

Agriculture

Contact Information for Business Card

CORALBEND PASTORAL TRADERS

Colors

Designer to choose colors to be used in the design.

Requirements
Must have
• Company Logo

```html
<!DOCTYPE html>
<html lang="en">
<head>
<meta charset="utf-8">
<title>Coralbend Pastoral Traders – Business Cards</title>
<link href="https://fonts.googleapis.com/css2?family=Montserrat:wght@400;500;700&display=swap" rel="stylesheet">
<style>
  :root {
    --stage: #2b2b2b;
    --burgundy: #650c24;
    --burgundy-deep: #540819;
    --crimson: #7d1519;
    --ink: #2a2a2a;
    --name: #5a0f24;
    --paper: #ffffff;
  }
  * { margin: 0; padding: 0; box-sizing: border-box; }
  html, body { width: 1200px; height: 1059px; overflow: hidden; }
  body {
    background: var(--stage);
    font-family: "Montserrat", sans-serif;
    position: relative;
  }
  .card {
    position: absolute;
    border-radius: 18px;
    overflow: hidden;
  }
  .card-front {
    left: 256px; top: 89px; width: 689px; height: 390px;
    background: var(--burgundy);
  }
  .card-back {
    left: 252px; top: 546px; width: 696px; height: 395px;
    background: var(--paper);
  }
  .brand {
    position: absolute;
    display: flex;
    align-items: center;
    font-weight: 700;
  }
  .brand-mark {
    border-radius: 50%;
    flex: none;
  }
  .brand-name { display: flex; flex-direction: column; line-height: 1; }
  .brand-front {
    left: 62px; top: 125px; gap: 22px;
    color: var(--burgundy-deep);
  }
  .brand-front .brand-mark { width: 96px; height: 96px; background: var(--burgundy-deep); }
  .brand-front .line-1 { font-size: 58px; letter-spacing: 1px; }
  .brand-front .line-2 { font-size: 25px; letter-spacing: 6px; margin-top: 10px; }

  .brand-back {
    left: 298px; top: 118px; gap: 12px;
    color: var(--name);
  }
  .brand-back .brand-mark { width: 56px; height: 56px; background: var(--name); }
  .brand-back .line-1 { font-size: 35px; letter-spacing: 0.5px; }
  .brand-back .line-2 { font-size: 14.6px; letter-spacing: 3.6px; margin-top: 7px; }

  .holder { position: absolute; left: 36px; top: 32px; }
  .holder-name { font-size: 28px; font-weight: 700; color: var(--name); letter-spacing: 0.3px; }
  .holder-role { font-size: 18px; font-weight: 500; color: var(--ink); margin-top: 2px; }

  .contact { position: absolute; left: 35px; top: 160px; list-style: none; }
  .contact li {
    display: flex; align-items: center; gap: 6px;
    font-size: 19px; color: var(--ink); height: 25px;
  }
  .contact svg { width: 17px; height: 15px; fill: var(--name); }

  .address {
    position: absolute; left: 36px; top: 228px;
    font-size: 19px; color: var(--ink); line-height: 25px; font-style: normal;
  }
  .footer-wave { position: absolute; left: 0; top: 0; width: 696px; height: 395px; }
  .website {
    position: absolute; right: 28px; top: 340px;
    font-size: 18px; color: var(--paper); letter-spacing: 0.2px;
  }
</style>
</head>
<body>
  <section class="card card-front" aria-label="Card front">
    <div class="brand brand-front">
      <span class="brand-mark"></span>
      <span class="brand-name">
        <span class="line-1">CORALBEND</span>
        <span class="line-2">PASTORAL TRADERS</span>
      </span>
    </div>
  </section>

  <section class="card card-back" aria-label="Card back">
    <svg class="footer-wave" viewBox="0 0 696 395" aria-hidden="true">
      <path fill="var(--burgundy)" d="M0,348 C150,382 300,342 440,308 C540,292 620,287 696,286 L696,395 L0,395 Z"/>
      <path fill="var(--crimson)" d="M0,304 C80,334 200,346 436,307 C300,336 150,362 0,336 Z"/>
      <path fill="none" stroke="var(--paper)" stroke-width="3" d="M0,340 C140,372 300,346 440,307"/>
    </svg>

    <div class="holder">
      <h1 class="holder-name">DANIEL HARROW</h1>
      <p class="holder-role">Managing Director</p>
    </div>

    <ul class="contact">
      <li>
        <svg viewBox="0 0 24 20"><path d="M2,8 C2,3 22,3 22,8 L18,9 L17,6 C14,5 10,5 7,6 L6,9 Z M6,10 L8,7 H16 L18,10 V18 H6 Z M12,11 a3,3 0 1,0 0.01,0 Z"/></svg>
        <span>123 456 789</span>
      </li>
      <li>
        <svg viewBox="0 0 24 20"><path d="M2,7 L12,1 L22,7 V19 H2 Z M3,8 V18 L9,13 Z M21,8 L15,13 L21,18 Z M4,19 L12,12 L20,19 Z"/></svg>
        <span>info@coralbend.com</span>
      </li>
    </ul>

    <address class="address">Your address, City<br>State, Zip 1234</address>

    <div class="brand brand-back">
      <span class="brand-mark"></span>
      <span class="brand-name">
        <span class="line-1">CORALBEND</span>
        <span class="line-2">PASTORAL TRADERS</span>
      </span>
    </div>

    <p class="website">www.coralbend.com</p>
  </section>
</body>
</html>
```